Brightleaf Card Venture Flyer

I need a DL sized flyer that will be sent out to participants in our Brightleaf Card Venture - sharing 1million Brightleaf Cards with the world. This flyer will form the first tangible item most of our community will receive from Lifting the Horizon, so it needs to be able to communicate our goal of inspiring change, possibility, kindness and love in the world.

Target Market(s)

Women aged 30 - 50, sophisticated, generous, philanthropy minded, contemporary, elegant

Font styles to use
Sans Serif
Other font styles liked:
• Raleway

Colors

Designer to choose colors to be used in the design.

Requirements
Must have
• Must be DL size - i.e. one third of an A4. On one side the flyer must also include space for the Brightleaf Cards to be stuck - the brightleaf cards are Stikkas that are 3in (76mm) square.
• The logo must be included somewhere, along with the website and social media icons - liftingthehorizon.com.au, Facebook, Instagram, Twitter all @liftingthehorizon.
• The copy for the flyer is:
• Thank you so much for helping us to reach our goal of having one million brightleaf cards out in the world. Share one of our notes with a friend, a family member, with a total stranger, or perhaps just with yourself. And remember that you might just be Lifting the Horizon in someone else's day.
• Share the story of your brightleaf cards on social media with the hashtag #brightleafcardventure or send us a photo and your story to bcventure@liftingthehorizon.com.au

```html
<!DOCTYPE html>
<html lang="en">
<head>
<meta charset="utf-8">
<title>Brightleaf Card Venture Flyer</title>
<link rel="stylesheet" href="https://fonts.googleapis.com/css2?family=Bebas+Neue&family=Raleway:wght@400;500;700&display=swap">
<style>
  :root {
    --page: #ffffff;
    --paper: #ecd9b6;
    --paper-edge: #e2c89c;
    --ink: #3a2316;
    --band: #b98b57;
    --band-text: #fbf3e6;
    --sky-top: #0f2a4e;
    --sky-mid: #1f5a6e;
    --cloud: #efe7a8;
    --logo-text: #ffffff;
    --accent: #1f8a8a;
  }
  * { box-sizing: border-box; margin: 0; padding: 0; }
  html, body { width: 1200px; height: 1185px; overflow: hidden; background: var(--page); }
  .canvas { position: relative; width: 1200px; height: 1185px; }

  .flyer-front {
    position: absolute; left: 63px; top: 64px; width: 1074px; height: 512px; overflow: hidden;
  }
  .front-photo {
    position: absolute; inset: 0;
    background:
      radial-gradient(ellipse 60% 35% at 50% 105%, var(--cloud) 0%, rgba(239,231,168,0) 70%),
      linear-gradient(180deg, var(--sky-top) 0%, var(--sky-mid) 55%, #8fa78a 80%, var(--cloud) 100%);
  }
  .front-logo {
    position: absolute; right: 70px; top: 140px;
    font-family: "Raleway", sans-serif; font-weight: 500; font-size: 46px;
    color: var(--logo-text); letter-spacing: 1px;
  }

  .flyer-back {
    position: absolute; left: 63px; top: 610px; width: 1074px; height: 512px;
    background: linear-gradient(135deg, var(--paper) 0%, var(--paper-edge) 100%);
    color: var(--ink);
  }
  .message {
    position: absolute; left: 37px; top: 30px; width: 600px;
    font-family: "Bebas Neue", sans-serif; font-size: 26px; line-height: 40px; letter-spacing: 0.3px;
  }
  .message .inline-logo {
    font-family: "Raleway", sans-serif; font-weight: 700; font-size: 20px;
    color: var(--accent); letter-spacing: 0; padding: 0 10px;
  }
  .message .gap { display: block; height: 0; }
  .share-note {
    position: absolute; left: 37px; top: 352px; width: 440px;
    font-family: "Raleway", sans-serif; font-size: 13.5px; line-height: 27px;
  }
  .share-note strong { font-weight: 700; }
  .share-note .email { font-weight: 700; text-decoration: underline; }
  .social {
    position: absolute; left: 474px; top: 368px; width: 150px; text-align: center;
    font-family: "Raleway", sans-serif; font-size: 11px; font-weight: 500;
  }
  .social svg { display: block; margin: 0 auto 6px; }
  .card-spot {
    position: absolute; left: 655px; top: 34px; width: 389px; height: 388px;
    border: 1.5px dashed #8a6a52;
  }
  .site-band {
    position: absolute; left: 0; bottom: 0; width: 100%; height: 58px; background: var(--band);
    display: flex; align-items: center; justify-content: center;
    font-family: "Raleway", sans-serif; font-size: 21px; letter-spacing: 6px; color: var(--band-text);
  }
</style>
</head>
<body>
<div class="canvas">
  <section class="flyer-front">
    <div class="front-photo" role="img" aria-label="Photo of a child with a homemade bottle jetpack flying above clouds under a night sky with a crescent moon"></div>
    <div class="front-logo">Lifting the Horizon</div>
  </section>

  <section class="flyer-back">
    <p class="message">
      Thank you so much for helping us to reach our goal of having
      one million brightleaf cards out in the world.<br>
      Share one of our notes with a friend, a family member, with
      a total stranger, or perhaps just with yourself.<br>
      And remember that<br>
      you might just be <span class="inline-logo">Lifting the Horizon</span> in someone else's day.
    </p>

    <p class="share-note">
      Share the story of your brightleaf cards on social media
      with the hashtag <strong>#brightleafcardventure</strong> or send us a photo
      and your story to <span class="email">bcventure@liftingthehorizon.com.au</span>
    </p>

    <div class="social">
      <svg width="140" height="42" viewBox="0 0 140 42" aria-hidden="true">
        <circle cx="21" cy="21" r="19" fill="none" stroke="#3a2316" stroke-width="2"/>
        <circle cx="70" cy="21" r="19" fill="none" stroke="#3a2316" stroke-width="2"/>
        <circle cx="119" cy="21" r="19" fill="none" stroke="#3a2316" stroke-width="2"/>
      </svg>
      all@liftingthehorizon
    </div>

    <div class="card-spot" aria-label="Space for a brightleaf card"></div>

    <div class="site-band">liftingthehorizon.com.au</div>
  </section>
</div>
</body>
</html>
```